QRV (Guaranteed Project)

**Note: The girl image is not mandatory, that was just an idea, it may even look better with just text and no girl

TEXT (Lorne Bexley and Vantro logos large please):

PEOPLE GET READY (the font from the image below for people get ready looks good, kind of retro)

QRV WEEKEND 2014
SUNDAY MAY 25

430-9pm

QRV after party starts at 9pm-2am

Featuring
LORNE BEXLEY (SF) (use logo, largest name)
VANTRO (Sac) (use logo w/out the text below it, and slightly smaller than lorne bexley)

at K@Z Uptown 2847 J Street 21+

Project Deadline Extended
Reason: The mgr wants to review them and hasn't said yes yet.

Target Market(s)

House/Electronic Music Night Club

Font styles to use
Sans Serif

Colors
ec2027
ffffff

Requirements
Nice to have
• Would look nice with the red background and maybe a reddish filter on the girl

```html
<!DOCTYPE html>
<html lang="en">
<head>
<meta charset="utf-8">
<title>People Get Ready – QRV Weekend 2014</title>
<link rel="stylesheet" href="https://fonts.googleapis.com/css2?family=Londrina+Solid:wght@900&family=Fredoka:wght@600&display=swap">
<style>
  :root {
    --brand-red: #ec2027;
    --poster-red: #e8464e;
    --photo-light: #f07a7d;
    --photo-mid: #ea5f66;
    --ink: #ffffff;
  }
  html, body {
    margin: 0;
    padding: 0;
    width: 939px;
    height: 1200px;
    overflow: hidden;
    background: var(--poster-red);
  }
  .poster {
    display: block;
    width: 939px;
    height: 1200px;
  }
  .poster__bg { fill: var(--poster-red); }
  .poster__photo { fill: url(#photoTint); }
  .headline {
    font-family: "Londrina Solid", "Arial Narrow", sans-serif;
    font-weight: 900;
    fill: var(--ink);
  }
  .info {
    font-family: "Fredoka", "Arial Rounded MT Bold", sans-serif;
    font-weight: 600;
    fill: var(--ink);
  }
  .lineup__mark { fill: none; stroke: var(--ink); stroke-width: 4; }
</style>
</head>
<body>
<svg class="poster" viewBox="0 0 939 1200" xmlns="http://www.w3.org/2000/svg">
  <defs>
    <radialGradient id="photoTint" cx="0.6" cy="0.4" r="0.62">
      <stop offset="0" stop-color="#f07a7d"/>
      <stop offset="0.6" stop-color="#ea5f66"/>
      <stop offset="1" stop-color="#e8464e"/>
    </radialGradient>
  </defs>

  <rect class="poster__bg" x="0" y="0" width="939" height="1200"/>
  <rect class="poster__photo" x="260" y="0" width="679" height="1100" role="img" aria-label="Close-up photo of a woman, tinted red, behind the headline"/>

  <g class="headline">
    <text x="55" y="236" font-size="278" textLength="821" lengthAdjust="spacingAndGlyphs">PEOPLE</text>
    <text x="55" y="352" font-size="108" textLength="235" lengthAdjust="spacingAndGlyphs">GET</text>
    <text x="55" y="548" font-size="229" textLength="767" lengthAdjust="spacingAndGlyphs">READY</text>
  </g>

  <g class="info">
    <text x="44" y="650" font-size="70" textLength="206" lengthAdjust="spacingAndGlyphs">SUNDAY</text>
    <text x="290" y="751" font-size="195" textLength="187" lengthAdjust="spacingAndGlyphs">25</text>
    <text x="44" y="743" font-size="115" textLength="214" lengthAdjust="spacingAndGlyphs">MAY</text>
    <text x="44" y="830" font-size="69" textLength="269" lengthAdjust="spacingAndGlyphs">430–9pm</text>
    <text x="336" y="830" font-size="19" textLength="407" lengthAdjust="spacingAndGlyphs">QRV after party starts at 9pm–2am</text>
  </g>

  <g class="info">
    <text x="44" y="939" font-size="103" textLength="856" lengthAdjust="spacingAndGlyphs">QRV WEEKEND 2014</text>
    <text x="44" y="1009" font-size="79" textLength="856" lengthAdjust="spacingAndGlyphs">HOUSE MUSIC AT ITS FINEST</text>
    <text x="44" y="1080" font-size="69" textLength="850" lengthAdjust="spacingAndGlyphs">K@Z Uptown 2847 J Street 21+</text>
  </g>

  <g class="lineup info">
    <text x="44" y="1118" font-size="22" letter-spacing="2">FEATURING</text>
    <circle class="lineup__mark" cx="64" cy="1158" r="20"/>
    <text x="96" y="1176" font-size="52" textLength="380" lengthAdjust="spacingAndGlyphs">LORNE BEXLEY</text>
    <text x="500" y="1170" font-size="22" textLength="120" lengthAdjust="spacingAndGlyphs">NORVANE</text>
    <text x="650" y="1176" font-size="46" textLength="250" lengthAdjust="spacingAndGlyphs">VANTRO</text>
  </g>
</svg>
</body>
</html>
```